MS word document templates for consultancy

I need the following templates for my business using my logo as branding.

- General report template
- Letter head template
- Tender proposal template

The templates should be sleek and with minimal colors, but with a small amount of green and grey where appropriate (as per attached logo and email signature). Font should be consistent with the text in the email signature.

```html
<!DOCTYPE html>
<html lang="en">
<head>
<meta charset="utf-8">
<title>Northpath Group – Letterhead Templates</title>
<link rel="stylesheet" href="https://fonts.googleapis.com/css2?family=Noto+Sans:wght@400;600;700&display=swap">
<style>
  :root{
    --page:#f7f7f7;
    --strip:#e3f0e6;
    --gap:#ffffff;
    --ink:#151515;
    --grey:#6f6f6f;
    --green:#1f9a3e;
    --faint:#e7e8ea;
    --card:#ffffff;
  }
  *{margin:0;padding:0;box-sizing:border-box}
  html,body{width:1200px;height:811px;overflow:hidden;background:var(--gap)}
  body{position:relative;font-family:"Noto Sans",Arial,sans-serif;color:var(--ink)}
  .page{position:absolute;top:0;height:811px;width:549px;background:var(--page)}
  .page--first{left:0}
  .page--second{left:610px}
  .edge-strip{position:absolute;top:0;height:811px;width:41px;background:var(--strip)}
  .edge-strip--first{left:549px}
  .edge-strip--second{left:1159px}

  .brand-name{position:absolute;top:31px;right:25px;font-size:25px;font-weight:400;letter-spacing:.3px;color:var(--ink);white-space:nowrap}
  .brand-watermark{position:absolute;left:0;right:0;text-align:center;font-size:54px;font-weight:400;color:var(--faint);white-space:nowrap;letter-spacing:.5px}
  .page--first .brand-watermark{top:334px;padding-left:20px}
  .page--second .brand-watermark{top:340px;padding-left:40px}

  .signature{position:absolute;background:var(--card)}
  .signature .person{font-weight:700;color:var(--ink)}
  .signature .role{font-weight:600;color:var(--grey)}
  .signature .rule{background:repeating-linear-gradient(90deg,var(--ink) 0 2.2px,transparent 2.2px 3px)}
  .signature .phone{font-weight:700;color:var(--green)}

  .signature--footer{left:399px;top:719px;width:121px;height:73px;font-size:7.8px;line-height:10.2px}
  .signature--footer .rule{width:80px;height:1px;margin:4.5px 0 4.5px}
  .signature--footer .phone{margin-top:0}
  .signature--footer .sig-brand{margin-top:6px;font-size:14px;line-height:16px;font-weight:400;color:var(--ink);white-space:nowrap}

  .signature--header{left:628px;top:39px;width:203px;height:79px;padding-top:3px;font-size:12.6px;line-height:17px}
  .signature--header .rule{width:133px;height:1.5px;margin:8px 0 7.5px}
</style>
</head>
<body>
  <section class="page page--first">
    <div class="brand-name">Northpath Group</div>
    <div class="brand-watermark">Northpath Group</div>
    <div class="signature signature--footer">
      <div class="person">Jordan Ellery</div>
      <div class="role">Managing Director</div>
      <div class="rule"></div>
      <div class="phone">P: 0400 555 019</div>
      <div class="sig-brand">Northpath Group</div>
    </div>
  </section>
  <div class="edge-strip edge-strip--first"></div>

  <section class="page page--second">
    <div class="brand-name">Northpath Group</div>
    <div class="brand-watermark">Northpath Group</div>
  </section>
  <div class="signature signature--header">
    <div class="person">Jordan Ellery</div>
    <div class="role">Managing Director</div>
    <div class="rule"></div>
    <div class="phone">P: 0400 555 019</div>
  </div>
  <div class="edge-strip edge-strip--second"></div>
</body>
</html>
```